Kelvaro Guest Event Collateral

Create a double-sided, oversized piece of collateral for a series of guest networking events that we'll be hosting in 2019

We are looking for this piece of collateral to be the size of an oversized post card (1/2 of an 8/5 x 11 piece of paper). The front should include the following: Kelvaro's Mission Statement: Continually foster a culture of community and education for focused business professionals. How do we do it? Using four distinct principles, Kelvaro offers business professionals the opportunity to be successful right now ,as well as next year. Through in-person meetings, virtual meetings, networking events, and educational opportunities Kelvaro offers members a chance to hit their goals not only this year, but every year! Collaboration: Work with like-minded, driven Kelvaro members to collaborate and overcome the objections, hurdles and challenges that all business professionals face, either in person at twice monthly meetings, or virtually, from the comfort of your home or office. Accountability: Stay on track, and complete the goals you have set for yourself! Weekly in person or virtual meetings afford all members the opportunity to review their plan twice a month with fellow Kelvaro members, and trained Kelvaro coaches. Referrals: In the midst of crafting an executable, measurable and attainable plan let Kelvaro build your business through a steady stream of referrals via six yearly networking events, specifically designed to ensure you walk away with new referral partners. Strategy: Let Kelvaro assist you in crafting a strategy within our proven business planning template; realistic, understandable, measurable, beyond normal, attainable and time bound. The back should include the following: Become a Kelvaro member for $150/month and join us for 6 Networking Events in 2019 plus much more! We aren’t just about collaboration, accountability and strategy! Creating opportunities for referrals is also a cornerstone of Kelvaro! To make certain we are delivering on this principle, Kelvaro will host 6 events throughout 2019, complete with specific activities at each event to ensure you meet everyone in the room, making immediate connects to build your referral network. Join now and put yourself in position for success in 2019! Name: Phone: Email: Company Name: Industry: Position: Credit Card Number: Exp. Date: Testimonials: Overall I think people are lazy. I know I am! The benefits I have found and have come to truly appreciate thru Kelvaro are a sense of professionalism, accountability and shared enthusiasm. These things break that cycle of laziness for me and, I am sure, many others. When I walk into a meeting I know that positive and helpful feedback is the name of the game. Feedback from others and in many other industries from my own has become a key and cornerstone to my business and personal success. I would urge anyone no matter what your occupation to attend a couple of meetings and see how this group of like minded professionals can help you to achieve more. More time, More success, More health, More security, More money, More happiness..............What could you use more of? Gordon T. Mabry Sr. Automotive Consultant Bramblewick Leasing & Sales Thank you!

Target Market(s)

Small business owners, entrpreneurs, networkers, sales people

Industry/Entity Type

Business Consultant

Font styles to use
Sans Serif

Colors
f36f22
f68d4e
f8ba93
f78f20
faa54b

Requirements
Must have
• - Imagery
• - Our company logo
• - Clear CTA to check out our website (www.kelvaro-example.com)
• - Option to "Join the Kelvaro Community Today!" and include a spot for someone to fill in their name, email address, company name, and phone number
• - Reference that we host 6+ networking events in Denver throughout the year that are free to attend and are unlike any other networking event they've attended before
• - Mention that we have in-person meetings 2x per month, virtual meeting options, networking events, and educational events
• - Highlight the following acronym which references our core company components:
• Collaboration:
• Work with like-minded, driven Kelvaro members to collaborate and overcome the objections, hurdles and challenges that all business professionals face, in either in person twice monthly meetings, or virtually, from the comfort of your home of office.
• Accountability:
• Stay on track, and complete the goals you have set for yourself! Weekly in person or virtual meetings afford all members the opportunity to review their plan twice a month with your fellow Kelvaro members and trained Kelvaro coaches, to make certain you success is continuous throughout the year.
• Referrals:
• In the midst of crafting an executable, measurable and attainable plan let Kelvaro build your business through a steady stream of referral opportunities via twelve yearly networking events, specifically designed to ensure you walk away with new referral partners.
• Strategy:
• Let Kelvaro assist you in crafting a strategy within our proven business planning template; realistic, understandable, measurable, beyond normal, attainable and time bound.

```html
<!DOCTYPE html>
<html lang="en">
<head>
<meta charset="utf-8">
<title>Kelvaro Guest Event Collateral</title>
<link href="https://fonts.googleapis.com/css2?family=Montserrat:wght@300;400;500;700;800&display=swap" rel="stylesheet">
<style>
  :root {
    --bg: #f6b891;
    --orange-deep: #f36f22;
    --orange: #f68d4e;
    --orange-warm: #f78f20;
    --orange-light: #faa54b;
    --peach: #f8ba93;
    --field: #f6e2d2;
    --paper: #f1f0f4;
    --ink: #231f20;
    --navy: #1e2a38;
    --text: #2b2b2b;
  }
  * { margin: 0; padding: 0; box-sizing: border-box; }
  html, body { width: 1200px; height: 1200px; overflow: hidden; }
  body {
    background: var(--bg);
    font-family: "Montserrat", sans-serif;
    color: var(--text);
    position: relative;
  }
  .sheet {
    position: absolute;
    background: var(--paper);
    overflow: hidden;
  }
  .sheet--front { left: 56px; top: 153px; width: 522px; height: 736px; }
  .sheet--back { left: 635px; top: 150px; width: 521px; height: 734px; }
  .abs { position: absolute; }

  /* front */
  .brand {
    left: 264px; top: 27px;
    display: flex; align-items: center; gap: 7px;
    font-size: 25px; font-weight: 400; color: #4a4a4a; letter-spacing: 0.5px;
  }
  .brand__square { width: 22px; height: 22px; background: var(--orange-warm); }
  .hero { left: 0; top: 48px; }
  .hero-mark { left: 18px; top: 82px; width: 62px; height: 62px; background: var(--ink); }
  .headline {
    font-weight: 800; color: var(--ink);
    font-size: 28px; line-height: 39.5px;
    white-space: nowrap;
  }
  .front-headline { left: 16px; top: 170px; }
  .section-title {
    font-size: 12.5px; font-weight: 800; color: var(--orange-deep); letter-spacing: 0.2px;
  }
  .body-copy { font-size: 8.5px; line-height: 11.4px; text-align: justify; }
  .company { left: 16px; top: 467px; width: 249px; }
  .company .body-copy { margin-top: 10px; }
  .company .body-copy + .body-copy { margin-top: 11px; }
  .why { left: 283px; top: 467px; width: 221px; }
  .why ul { list-style: none; margin-top: 10px; font-size: 8.1px; line-height: 10.4px; }
  .why li { position: relative; padding-left: 11px; margin-bottom: 9px; }
  .why li svg { position: absolute; left: 0; top: 2px; }
  .cta-band { left: 0; top: 629px; width: 522px; height: 107px; background: var(--orange-light); }
  .cta-band__lead {
    position: absolute; left: 0; top: 0; width: 197px; height: 107px;
    background: var(--orange-deep); color: #fff; padding: 12px 0 0 17px;
  }
  .cta-title { font-size: 17px; font-weight: 800; line-height: 18px; }
  .cta-title .spaced { letter-spacing: 6px; display: block; }
  .cta-url { font-size: 12px; font-weight: 400; margin-top: 12px; white-space: nowrap; }
  .form-row { position: absolute; left: 210px; width: 296px; height: 19px; display: flex; align-items: center; }
  .form-row label { width: 86px; font-size: 9.4px; color: var(--ink); white-space: nowrap; }
  .form-row .field { width: 210px; height: 19px; background: var(--field); }

  /* back */
  .back-hero { left: 0; top: 0; }
  .back-mark { left: 21px; top: 85px; width: 62px; height: 62px; background: var(--orange-warm); }
  .back-headline { left: 19px; top: 212px; font-size: 28px; line-height: 35px; }
  .pillar { position: absolute; }
  .pillar__icon {
    position: absolute; left: 0; top: 0; width: 58px; height: 58px;
    background: var(--orange-light);
    clip-path: polygon(0 0, 100% 0, 100% 78%, 78% 100%, 0 100%);
  }
  .pillar__icon svg { position: absolute; left: 13px; top: 13px; }
  .pillar__text { position: absolute; left: 68px; top: 0; width: 162px; }
  .pillar__title { font-size: 13.5px; font-weight: 700; color: var(--orange-deep); line-height: 16px; }
  .pillar__body { font-size: 7.8px; line-height: 10.4px; text-align: justify; margin-top: 2px; }
  .pillar--collab { left: 18px; top: 385px; }
  .pillar--referrals { left: 267px; top: 382px; }
  .pillar--account { left: 18px; top: 505px; }
  .pillar--strategy { left: 267px; top: 502px; }
  .closing { left: 0; top: 626px; width: 521px; height: 98px; background: var(--orange-light); padding: 12px 18px 0; }
  .closing__title { font-size: 13.6px; font-weight: 800; color: var(--ink); }
  .closing__body { font-size: 8.7px; line-height: 15.8px; color: var(--ink); margin-top: 3px; }
  .closing-rule { left: 0; top: 724px; width: 521px; height: 10px; background: var(--navy); }
</style>
</head>
<body>

<section class="sheet sheet--front">
  <div class="abs brand"><span class="brand__square"></span>KELVARO</div>

  <svg class="abs hero" width="522" height="392" viewBox="0 0 522 392">
    <defs>
      <linearGradient id="meetingTones" x1="0" y1="0" x2="1" y2="1">
        <stop offset="0" stop-color="#5a4a46"/>
        <stop offset="0.45" stop-color="#b07a4c"/>
        <stop offset="1" stop-color="#3c3a4a"/>
      </linearGradient>
    </defs>
    <polygon points="174.4,28.8 521.6,28.8 521.6,39.2 177.6,39.2" fill="var(--orange-deep)"/>
    <polygon points="184,39.2 521.6,39.2 521.6,391.2 292.8,391.2" fill="url(#meetingTones)" role="img" aria-label="Overhead photo of professionals meeting around a wooden table with laptops and notes"/>
    <polygon points="0,0 126.4,0 240,349.6 0,349.6" fill="var(--orange)"/>
    <polygon points="126.4,0 177.6,0 292.8,391.2 232,391.2" fill="var(--navy)" opacity="0.9"/>
  </svg>
  <div class="abs hero-mark"></div>
  <h1 class="abs headline front-headline">Learn<br>simple<br>strategies<br>to ensure<br>your success</h1>

  <div class="abs company">
    <h2 class="section-title">THE COMPANY</h2>
    <p class="body-copy">We founded Kelvaro with one objective: Help sales professionals, business owners, and entrepreneurs take a step away from the myriad daily distractions so they can create a simple, actionable business strategy.</p>
    <p class="body-copy">Confused by all the competing theories, terminologies, and processes? We distill these down into an easily digestible approach that allows for broad application regardless of your position, tenure, or industry.</p>
  </div>

  <div class="abs why">
    <h2 class="section-title">WHY JOIN US?</h2>
    <ul class="body-copy">
      <li><svg width="9" height="8" viewBox="0 0 9 8"><path d="M1 4 L3.5 6.5 L8 1" fill="none" stroke="var(--orange-deep)" stroke-width="1.8"/></svg>We host 6+ networking events in Denver throughout the year that are free to attend and are unlike any other networking event you've attended before.</li>
      <li><svg width="9" height="8" viewBox="0 0 9 8"><path d="M1 4 L3.5 6.5 L8 1" fill="none" stroke="var(--orange-deep)" stroke-width="1.8"/></svg>We have in-person meetings twice a month, virtual meeting options, networking events, and educational events.</li>
      <li><svg width="9" height="8" viewBox="0 0 9 8"><path d="M1 4 L3.5 6.5 L8 1" fill="none" stroke="var(--orange-deep)" stroke-width="1.8"/></svg>We assist members in the creation of a simple and easy-to-execute plan. This approach ensures that members stay focused on and committed to the activities that matter and deliver results.</li>
    </ul>
  </div>

  <div class="abs cta-band">
    <div class="cta-band__lead">
      <p class="cta-title">Join the Kelvaro <span class="spaced">Community</span>Today!</p>
      <p class="cta-url">www.kelvaro-example.com</p>
    </div>
    <div class="form-row" style="top:10px"><label>Name:</label><span class="field"></span></div>
    <div class="form-row" style="top:31px"><label>Email Address:</label><span class="field"></span></div>
    <div class="form-row" style="top:52px"><label>Company Name:</label><span class="field"></span></div>
    <div class="form-row" style="top:73px"><label>Phone Number:</label><span class="field"></span></div>
  </div>
</section>

<section class="sheet sheet--back">
  <svg class="abs back-hero" width="521" height="351" viewBox="0 0 521 351">
    <defs>
      <linearGradient id="chartTones" x1="0" y1="0" x2="1" y2="1">
        <stop offset="0" stop-color="#e9e9ee"/>
        <stop offset="0.6" stop-color="#dcdde4"/>
        <stop offset="1" stop-color="#c9cbd4"/>
      </linearGradient>
    </defs>
    <polygon points="224.8,0 520.8,0 520.8,226.4 412.8,350.4 296.8,350.4 156.8,114.4" fill="url(#chartTones)" role="img" aria-label="Overhead photo of hands reviewing printed charts and reports on a desk"/>
    <polygon points="131.2,114.4 199.2,0 224.8,0 156.8,114.4" fill="var(--orange-light)"/>
    <polygon points="131.2,114.4 156.8,114.4 296.8,350.4 272.8,350.4" fill="var(--orange-deep)"/>
    <polygon points="412.8,350.4 520.8,226.4 520.8,350.4" fill="var(--orange-warm)"/>
  </svg>
  <div class="abs back-mark"></div>
  <h2 class="abs headline back-headline">Kelvaro<br>offers a<br>four-pronged<br>approach:</h2>

  <div class="pillar pillar--collab">
    <div class="pillar__icon"><svg width="32" height="32" viewBox="0 0 32 32" fill="none" stroke="#fff" stroke-width="2"><path d="M3 12 L10 6 L16 10 L22 6 L29 12 L18 24 L14 24 Z"/></svg></div>
    <div class="pillar__text">
      <h3 class="pillar__title">Collaboration</h3>
      <p class="pillar__body">Work with like-minded, driven Kelvaro members to collaborate and overcome the objections, hurdles and challenges that all business professionals face, in either in person twice monthly meetings, or virtually, from the comfort of your home of office.</p>
    </div>
  </div>

  <div class="pillar pillar--referrals">
    <div class="pillar__icon"><svg width="32" height="32" viewBox="0 0 32 32" fill="none" stroke="#fff" stroke-width="2"><circle cx="16" cy="10" r="4"/><path d="M10 26 V18 H22 V26"/><path d="M2 16 H7 M25 16 H30"/></svg></div>
    <div class="pillar__text">
      <h3 class="pillar__title">Referrals</h3>
      <p class="pillar__body">In the midst of crafting an executable, measurable and attainable plan let Kelvaro build your business through a steady stream of referral opportunities via twelve yearly networking events, specifically designed to ensure you walk away with new referral partners.</p>
    </div>
  </div>

  <div class="pillar pillar--account">
    <div class="pillar__icon"><svg width="32" height="32" viewBox="0 0 32 32" fill="none" stroke="#fff" stroke-width="2"><circle cx="10" cy="8" r="4"/><path d="M6 30 V16 H14 V30"/><path d="M20 30 V4 H30 L27 8 L30 12 H20"/></svg></div>
    <div class="pillar__text">
      <h3 class="pillar__title">Accountability</h3>
      <p class="pillar__body">Stay on track, and complete the goals you have set for yourself! Weekly in person or virtual meetings afford all members the opportunity to review their plan twice a month with your fellow Kelvaro members and trained Kelvaro coaches, to make certain you success is continuous throughout the year.</p>
    </div>
  </div>

  <div class="pillar pillar--strategy">
    <div class="pillar__icon"><svg width="32" height="32" viewBox="0 0 32 32" fill="none" stroke="#fff" stroke-width="2"><rect x="2" y="4" width="20" height="16"/><path d="M5 16 L10 11 L14 14 L19 8"/><circle cx="25" cy="14" r="3"/><path d="M21 30 V20 H29 V30"/></svg></div>
    <div class="pillar__text">
      <h3 class="pillar__title">Strategy</h3>
      <p class="pillar__body">Let Kelvaro assist you in crafting a strategy within our proven business planning template; realistic, understandable, measurable, beyond normal, attainable and time bound.</p>
    </div>
  </div>

  <div class="abs closing">
    <h3 class="closing__title">Kelvaro takes a fresh approach with business strategy</h3>
    <p class="closing__body">Kelvaro helps you adopt a singular focus that ensures you'll avoid the distractions that prevent success. Through the identification of key foundational principles, an achievable yearly goal, consistent accountability, and a score-keeping process, you'll build a road map to success that is simple to follow and simple to execute.</p>
  </div>
  <div class="abs closing-rule"></div>
</section>

</body>
</html>
```